A Real Estate Company Needs a Business Card Design

We need a business card design for a new company based in Boston MA called "Brellmont Real Estate LLC" we are a small company but we like a big corporate look, a simple, sleek, modern and progressive look. we would like the option of having a design that could include the real estate agents personal photo and also a design if the realtor decides not to have a photo. we do not have LOGO at this moment, please use any property look pic corporate with word" Brellmont Real Estate LLC" please see attached file as an example.

```html
<!DOCTYPE html>
<html lang="en">
<head>
<meta charset="utf-8">
<title>Brellmont Real Estate LLC – Business Cards</title>
<link rel="stylesheet" href="https://fonts.googleapis.com/css2?family=Cinzel:wght@400&family=Open+Sans:wght@400;600&display=swap">
<style>
  :root {
    --brown-dark: #4a2410;
    --brown: #5b2e14;
    --bar: #3f1d0c;
    --paper: #ffffff;
    --cream: #f3ece6;
    --ink: #3a1a0b;
    --stage: #e6e3df;
  }
  * { box-sizing: border-box; margin: 0; padding: 0; }
  html, body { width: 1200px; height: 1000px; overflow: hidden; }
  body {
    background: var(--stage);
    font-family: "Open Sans", Arial, sans-serif;
    color: var(--ink);
    position: relative;
  }
  .brand-band {
    position: absolute; left: 0; top: 0; width: 1200px; height: 126px;
    background: var(--brown-dark);
    display: flex; align-items: center; justify-content: center;
  }
  .brand-name {
    font-family: "Cinzel", Georgia, serif;
    font-weight: 400;
    color: var(--cream);
    text-align: center;
    line-height: 1.1;
  }
  .brand-band .brand-name { font-size: 24px; letter-spacing: 3px; }
  .card {
    position: absolute; left: 320px; width: 560px; height: 320px;
    box-shadow: 0 6px 18px rgba(0,0,0,.18);
    overflow: hidden;
  }
  .card-front { top: 170px; background: var(--paper); }
  .card-back { top: 550px; background: var(--brown); }

  .bar { position: absolute; background: var(--bar); height: 9px; }
  .bar-top-1 { left: 0; top: 22px; width: 250px; }
  .bar-top-2 { left: 0; top: 40px; width: 220px; }
  .bar-bottom-1 { right: 0; bottom: 40px; width: 220px; }
  .bar-bottom-2 { right: 0; bottom: 22px; width: 250px; }
  .bar-edge { left: 22px; bottom: 22px; width: 6px; height: 200px; }

  .front-logo {
    position: absolute; left: 60px; top: 100px; width: 210px;
    display: flex; align-items: center; gap: 10px;
  }
  .front-logo .brand-name { color: var(--ink); font-size: 19px; letter-spacing: 2px; text-align: left; }
  .logo-square { width: 12px; height: 12px; background: var(--ink); flex: none; }

  .divider {
    position: absolute; left: 290px; top: 80px; width: 1px; height: 170px;
    background: #8a7366;
  }
  .person { position: absolute; left: 315px; top: 86px; }
  .person-name { font-size: 26px; font-weight: 400; line-height: 1.1; }
  .person-title { font-size: 11px; letter-spacing: 1px; margin-top: 2px; }
  .contact { position: absolute; left: 315px; top: 168px; font-size: 13px; line-height: 1.55; }

  .back-logo {
    position: absolute; left: 0; right: 0; top: 105px;
    display: flex; justify-content: center; align-items: center; gap: 12px;
  }
  .back-logo .brand-name { font-size: 30px; letter-spacing: 3px; }
  .back-logo .logo-square { background: var(--cream); width: 14px; height: 14px; }
  .web { position: absolute; left: 0; right: 0; top: 190px; text-align: center; color: var(--cream); font-size: 14px; font-weight: 600; letter-spacing: .5px; }
</style>
</head>
<body>
  <header class="brand-band">
    <div class="brand-name">Brellmont Real Estate LLC</div>
  </header>

  <section class="card card-front">
    <span class="bar bar-top-1"></span>
    <span class="bar bar-top-2"></span>
    <span class="bar bar-bottom-1"></span>
    <span class="bar bar-bottom-2"></span>
    <div class="front-logo">
      <span class="logo-square"></span>
      <div class="brand-name">Brellmont Real Estate LLC</div>
    </div>
    <span class="divider"></span>
    <div class="person">
      <div class="person-name">YourName</div>
      <div class="person-title">TITLE</div>
    </div>
    <div class="contact">
      <div>P: (XXX) 123 1234</div>
      <div>A: Location</div>
      <div>E: name@domain.com</div>
    </div>
  </section>

  <section class="card card-back">
    <div class="back-logo">
      <span class="logo-square"></span>
      <div class="brand-name">Brellmont Real Estate LLC</div>
    </div>
    <div class="web">www.yourdomain.com</div>
  </section>
</body>
</html>
```